Webdesign für  IT-Dienstleistungen
Webdesign für IT-Dienstleistungen
Zielgruppe
Wir bieten IT-Dienstleistungen rund um Handy, PC, Laptop und ZEP.
Zielgruppe sind Privatkunden im unterschiedlichen Alter, die Beratung benötigen oder Probleme haben.
Die Leute werden teilweise nicht super IT-affin sein, also muss das Design gut und die usability einfach sein.
Aufgabenstellung
Anbei sind Logo und Visual die bereits erstellt wurden und verwendet werden können.
Inhalte von https://dev.vameko.com/start/ und https://dev.vameko.com/anfrage/ und das anmeldeformular: https://dev.vameko.com/mein-konto/ soll auch auf der Startseite ersichtlich sein
sollten die Startseite ergeben plus Bilder und Texte, wo auch Konversation mit dem Kunden angezeigt werden kann, wenn eingeloggt.
Die Seite sollte sowohl auf dem barrierearm und responsive sein.

```html
<!DOCTYPE html>
<html lang="de">
<head>
<meta charset="utf-8">
<title>Vameko – Meine Anfragen</title>
<link href="https://fonts.googleapis.com/css2?family=Mulish:wght@400;600;700;800&display=swap" rel="stylesheet">
<style>
:root{
  --green:#84a013;
  --green-tint:#f2f4e8;
  --grey-text:#6e6e6e;
  --grey-band:#ededed;
  --grey-head:#f7f7f7;
  --line:#dcdcdc;
  --white:#ffffff;
  --logo:#6a6c6e;
}
*{box-sizing:border-box;margin:0;padding:0}
html,body{width:1200px;height:4125px;overflow:hidden;background:var(--white)}
body{position:relative;font-family:"Mulish",sans-serif;color:var(--grey-text)}
.site-header{position:absolute;top:0;left:0;width:1200px;height:202px}
.brand{position:absolute;left:62px;top:40px;font-size:96px;font-weight:800;letter-spacing:4px;color:var(--logo);line-height:1;text-transform:uppercase}
.menu-toggle{position:absolute;left:1012px;top:62px;width:122px;height:74px;display:flex;flex-direction:column;justify-content:space-between}
.menu-toggle span{display:block;height:12px;background:var(--green)}
.page-title{position:absolute;top:202px;left:0;width:1200px;height:180px;background:var(--grey-band);display:flex;align-items:center;justify-content:center;font-size:72px;font-weight:600;color:var(--green);letter-spacing:1px}
.message{position:absolute;left:62px;width:1072px;border:3px solid #e2e2e2;border-radius:10px;overflow:hidden;box-shadow:0 3px 8px rgba(0,0,0,.08)}
.message-customer{top:440px;height:675px;background:var(--white)}
.message-agent{top:1178px;height:987px;background:var(--green-tint)}
.message-head{height:205px;display:flex;align-items:center;padding-left:45px}
.message-customer .message-head{background:var(--grey-head)}
.message-agent .message-head{background:var(--green);color:var(--white)}
.avatar{width:110px;height:110px;border-radius:50%;flex:none}
.avatar-customer{background:linear-gradient(180deg,#f3f3f3 0%,#7d9c1a 55%,#d9d9d9 100%)}
.avatar-agent{background:linear-gradient(160deg,#7a5a44,#d6b8a0 60%,#3b3b3b)}
.author{margin-left:45px}
.author-name{font-size:42px;font-weight:700;line-height:1.2}
.author-date{font-size:36px;line-height:1.3}
.author-date small{font-size:30px}
.message-body{padding:45px 60px 0 58px;font-size:44px;line-height:60px}
.message-agent .message-body{padding-left:55px}
.message-body p{margin-bottom:60px}
.message-body a{color:var(--green);text-decoration:underline}
.divider{position:absolute;left:62px;width:1072px;height:3px;background:var(--line)}
.divider-top{top:2236px}
.divider-footer{top:3920px;height:4px;background:#cfcfcf}
.reply-author{position:absolute;left:108px;top:2285px;display:flex;align-items:center}
.reply-author .author-name{font-size:42px;margin-left:45px}
.reply-form label.field-label{position:absolute;left:62px;top:2462px;font-size:42px;font-weight:700}
.comment-box{position:absolute;left:62px;top:2543px;width:1072px;height:550px;border:3px solid #d4d4d4;background:var(--white);resize:none}
.close-option{position:absolute;left:128px;top:3168px;display:flex;align-items:center;font-size:43px;font-weight:700;color:var(--green)}
.close-option input{width:28px;height:28px;margin-right:30px}
.submit{position:absolute;left:62px;top:3293px;width:1072px;height:105px;border:none;border-radius:8px;background:var(--green);color:var(--white);font-family:inherit;font-size:45px;font-weight:700;box-shadow:0 4px 8px rgba(0,0,0,.18)}
.contact{position:absolute;left:0;width:1200px;display:flex;justify-content:center;align-items:center;font-size:64px;font-weight:700;color:var(--grey-text)}
.contact svg{margin-right:32px}
.contact-phone{top:3555px;height:100px}
.contact-mail{top:3680px;height:100px}
.legal{position:absolute;top:3995px;left:0;width:1200px;text-align:center;font-size:40px;color:#8a8a8a}
.legal span{margin:0 16px}
</style>
</head>
<body>
<header class="site-header">
  <div class="brand">Vameko</div>
  <div class="menu-toggle" aria-label="Menü"><span></span><span></span><span></span></div>
</header>

<h1 class="page-title">MEINE ANFRAGEN</h1>

<article class="message message-customer">
  <div class="message-head">
    <div class="avatar avatar-customer" role="img" aria-label="Illustrierter Avatar des Kunden"></div>
    <div class="author">
      <div class="author-name">Sie</div>
      <div class="author-date">18.10.2018 <small>um 13:25 Uhr</small></div>
    </div>
  </div>
  <div class="message-body">
    <p>Hallo!</p>
    <p>Ich habe ein Problem mit meinem Computer.</p>
    <p>Freundliche Grüsse,<br>Max Mustermann</p>
  </div>
</article>

<article class="message message-agent">
  <div class="message-head">
    <div class="avatar avatar-agent" role="img" aria-label="Profilfoto des Support-Mitarbeiters"></div>
    <div class="author">
      <div class="author-name">Lukas</div>
      <div class="author-date">18.10.2018 <small>um 13:25 Uhr</small></div>
    </div>
  </div>
  <div class="message-body">
    <p>Lorem ipsum dolor sit amet. Consectetur adipiscing elit, sed do eiusmod tempor incididunt ut labore et dolore magna aliqua.</p>
    <p>Ut enim ad minim veniam, quis nostrud exercitation ullamco laboris nisi ut aliquip ex ea commodo consequat.</p>
    <p>Duis aute irure <a href="#">dolor in reprehenderit</a> in voluptate velit esse cillum dolore eu fugiat nulla pariatur.</p>
  </div>
</article>

<div class="divider divider-top"></div>

<form class="reply-form">
  <div class="reply-author">
    <div class="avatar avatar-customer" role="img" aria-label="Illustrierter Avatar des Kunden"></div>
    <div class="author-name">Sie</div>
  </div>
  <label class="field-label" for="comment">Neuer Kommentar:</label>
  <textarea class="comment-box" id="comment"></textarea>
  <label class="close-option"><input type="checkbox">Problem ist gelöst, Anfrage schliessen</label>
  <button class="submit" type="button">Absenden</button>
</form>

<div class="contact contact-phone">
  <svg width="62" height="95" viewBox="0 0 62 95" aria-hidden="true">
    <rect x="3" y="3" width="56" height="89" rx="9" fill="none" stroke="#84a013" stroke-width="6"/>
    <rect x="10" y="14" width="42" height="60" fill="#84a013"/>
    <circle cx="31" cy="83" r="4" fill="#84a013"/>
  </svg>
  0041612049876
</div>
<div class="contact contact-mail">
  <svg width="80" height="60" viewBox="0 0 80 60" aria-hidden="true">
    <rect x="0" y="0" width="80" height="60" rx="5" fill="#84a013"/>
    <path d="M4 6 L40 34 L76 6" fill="none" stroke="#fff" stroke-width="6"/>
  </svg>
  support@vameko.com
</div>

<div class="divider divider-footer"></div>
<nav class="legal">AGB<span>|</span>Datenschutz<span>|</span>Impressum</nav>
</body>
</html>
```